Zelmor Harbor Advisors Website

We are interested in developing a complete website and long term maintenance with the developer we choose through this contest.

Zelmor is a financial consulting company. We will have a website that capitalizes on the initial costs of retaining a client by providing additional services the client needs and tyically spend using 3rd parties.

The primary function of the website will be structured as a sales tool to retain and provide financial services to the client. Also, to provide other services that are integral to starting, building, and growing a business in order to increase creditibility and maintain client loyalty.

Through a combination of in-house "white label" services as well well chosen outside professional services as "affiliates".

The website home page must be a an instant curb-side appeal and representation of our desired extraordinary image. That image is a robust, innovative (Zelmor), with a sophistication that creates an instant emotion of excitement and confidence that they have finally found that "needle in the haystack" they have been seeking. The feeling that they are compelled to take action lest they lose our contact information and are doomed to sink to the mediocrity that most business accept through a lack of effort and forsite.
Updates

Reason: Emails were going to the wrong account and I didn't receive any notices of questions or designs being posted.

Target Market(s)

Startup, growth and advancing companies seeking capital and other business services such as website and corporate image design, legal, marketing, asset management, investment and business consulting, etc.

Industry/Entity Type

Financial

Requirements
Must have
• We want to see your creativity
Nice to have
Should not have

```html
<!DOCTYPE html>
<html lang="en">
<head>
<meta charset="utf-8">
<title>Zelmor – Zelmor Harbor Advisors</title>
<link href="https://fonts.googleapis.com/css2?family=Arimo:wght@400;700&family=Open+Sans:wght@400;600&display=swap" rel="stylesheet">
<style>
  :root{
    --orange:#e2570d;
    --orange-light:#f27a2e;
    --blue:#1767c4;
    --blue-light:#3f8ddc;
    --link:#1a63b8;
    --text:#333333;
    --brand-text:#3a3a3a;
    --panel-border:#dcdcdc;
    --header-top:#ffffff;
    --header-bottom:#dedede;
    --footer-top:#f4f4f4;
    --footer-bottom:#dcdcdc;
  }
  *{box-sizing:border-box;margin:0;padding:0}
  html,body{width:1200px;height:902px;overflow:hidden;background:#fff}
  body{font-family:"Arimo",Arial,sans-serif;color:var(--text)}
  .page{position:relative;width:1200px;height:902px;overflow:hidden;
    background:linear-gradient(#fff 0,#fff 233px,#f2f2f2 233px,#f7f7f7 270px,#fff 300px)}

  /* header */
  .site-header{position:absolute;left:0;top:0;width:1200px;height:59px;
    background:linear-gradient(var(--header-top),var(--header-bottom));
    border-bottom:1px solid #c8c8c8}
  .brand{position:absolute;left:30px;top:0;height:58px;display:flex;align-items:center}
  .brand-name{font-family:"Arimo",sans-serif;font-size:34px;font-weight:400;color:var(--brand-text);line-height:40px}
  .main-nav{position:absolute;left:261px;top:0;display:flex;gap:2px}
  .main-nav a{display:block;width:181px;height:58px;line-height:56px;text-align:center;
    color:#fff;text-decoration:none;font-family:"Arimo",sans-serif;font-size:15px;
    border-radius:0 0 8px 8px;background:linear-gradient(var(--blue-light),var(--blue))}
  .main-nav a.active{background:linear-gradient(var(--orange-light),var(--orange))}

  /* hero */
  .hero{position:absolute;left:28px;top:84px;width:1146px;height:307px;border-radius:12px;
    border:1px solid #d0d0d0;box-shadow:0 3px 6px rgba(0,0,0,.18);
    background:linear-gradient(90deg,#fff 0%,#f6f6f6 55%,#efefef 100%);overflow:hidden}
  .hero-art{position:absolute;left:270px;top:5px;width:435px;height:300px;
    background:linear-gradient(100deg,#f1c84a 0%,#e9824a 35%,#62c75a 65%,#6fd46a 100%);
    opacity:.75;border-radius:6px}

  /* panels */
  .panel{position:absolute;top:424px;width:363px;height:411px;background:#fff;
    border:1px solid var(--panel-border);border-radius:12px;box-shadow:0 1px 5px rgba(0,0,0,.15)}
  .panel-welcome{left:33px}
  .panel-services{left:419px}
  .panel-testimonials{left:804px}
  .panel-head{position:absolute;left:6px;top:6px;width:351px;height:61px;border-radius:8px 8px 0 0;
    display:flex;align-items:center;justify-content:space-between;padding:0 12px 0 22px}
  .panel-head.orange{background:linear-gradient(var(--orange-light),var(--orange))}
  .panel-head.blue{background:linear-gradient(var(--blue-light),var(--blue))}
  .panel-head h2{font-family:"Open Sans",sans-serif;font-weight:400;font-size:30px;color:#fff}
  .panel-body{position:absolute;left:14px;top:84px;width:333px}
  .intro{font-size:14px;line-height:21px;text-align:justify}
  .service-list{list-style:none;padding:0 2px 0 6px}
  .service-list li{height:35px;line-height:37px;border-bottom:1px dotted #9aa9bb;font-size:14px;color:var(--link);
    display:flex;align-items:center;gap:8px}
  .service-list li:last-child{border-bottom:none}
  .service-list svg{flex:none}
  .quotes{list-style:none;padding:6px 0 0 10px}
  .quotes li{display:flex;gap:8px;margin-bottom:18px;font-size:14px;line-height:16.5px}
  .quotes .who{color:var(--link)}
  .quotes .when{color:#333}
  .read-more{position:absolute;right:14px;bottom:20px;width:97px;height:35px;border-radius:8px;
    background:linear-gradient(var(--orange-light),var(--orange));color:#fff;font-size:13px;
    text-align:center;line-height:35px;text-decoration:none;border:1px solid #c84b0a}

  /* footer */
  .site-footer{position:absolute;left:0;top:857px;width:1200px;height:45px;
    background:linear-gradient(var(--footer-top),var(--footer-bottom));border-top:1px solid #ccc;
    font-size:13px;color:#222;display:flex;align-items:center;justify-content:space-between;padding:0 27px}
  .footer-nav a{color:#222;text-decoration:none}
  .footer-nav span{margin:0 10px}
</style>
</head>
<body>
<div class="page">
  <header class="site-header">
    <div class="brand"><span class="brand-name">Zelmor</span></div>
    <nav class="main-nav">
      <a class="active" href="#">Home</a>
      <a href="#">About Us</a>
      <a href="#">Services</a>
      <a href="#">Solutions</a>
      <a href="#">Contact Us</a>
    </nav>
  </header>

  <section class="hero">
    <div class="hero-art" role="img" aria-label="3D block bar chart with a rising green arrow on a light grid"></div>
  </section>

  <section class="panel panel-welcome">
    <div class="panel-head orange">
      <h2>Welcome!</h2>
      <svg width="50" height="50" viewBox="0 0 50 50" aria-hidden="true">
        <ellipse cx="25" cy="21" rx="21" ry="17" fill="#bfe3fb" stroke="#fff" stroke-width="2"/>
        <path d="M14 34 L10 46 L24 37Z" fill="#bfe3fb" stroke="#fff" stroke-width="2"/>
      </svg>
    </div>
    <div class="panel-body">
      <p class="intro">Lorem Ipsum is simply dummy text of the printing and typesetting industry. Lorem Ipsum has been the industry's standard dummy text ever since the 1500s, when an unknown printer took a galley of type and scrambled it to make a type specimen book. It has survived not only five centuries, but also the leap into electronic typesetting, remaining essentially unchanged. It was popularised in the 1960s with the release of Pressfont sheets containing Lorem Ipsum passages, and more recently with desktop publishing software like Quillset PageBinder including versions of Lorem Ipsum.</p>
    </div>
    <a class="read-more" href="#">Read More</a>
  </section>

  <section class="panel panel-services">
    <div class="panel-head blue">
      <h2>Services</h2>
      <svg width="52" height="52" viewBox="0 0 52 52" aria-hidden="true">
        <g fill="#c9c9c9" stroke="#888" stroke-width="1">
          <circle cx="26" cy="26" r="17"/>
          <rect x="22" y="2" width="8" height="10"/><rect x="22" y="40" width="8" height="10"/>
          <rect x="2" y="22" width="10" height="8"/><rect x="40" y="22" width="10" height="8"/>
        </g>
        <circle cx="26" cy="26" r="8" fill="#1767c4" stroke="#777"/>
      </svg>
    </div>
    <div class="panel-body">
      <ul class="service-list">
        <li><svg width="7" height="8" viewBox="0 0 7 8"><path d="M0 0L7 4L0 8Z" fill="#2aa3e6"/></svg>Webdesign</li>
        <li><svg width="7" height="8" viewBox="0 0 7 8"><path d="M0 0L7 4L0 8Z" fill="#2aa3e6"/></svg>Capital Raising</li>
        <li><svg width="7" height="8" viewBox="0 0 7 8"><path d="M0 0L7 4L0 8Z" fill="#2aa3e6"/></svg>Legal, Accounting</li>
        <li><svg width="7" height="8" viewBox="0 0 7 8"><path d="M0 0L7 4L0 8Z" fill="#2aa3e6"/></svg>Financing, Sales Forces</li>
        <li><svg width="7" height="8" viewBox="0 0 7 8"><path d="M0 0L7 4L0 8Z" fill="#2aa3e6"/></svg>Printing</li>
      </ul>
    </div>
    <a class="read-more" href="#">Read More</a>
  </section>

  <section class="panel panel-testimonials">
    <div class="panel-head blue">
      <h2>Testimonials</h2>
      <svg width="52" height="54" viewBox="0 0 52 54" aria-hidden="true">
        <rect x="4" y="3" width="40" height="48" fill="#fff" stroke="#bbb"/>
        <g stroke="#aaa"><line x1="9" y1="16" x2="38" y2="16"/><line x1="9" y1="23" x2="38" y2="23"/><line x1="9" y1="30" x2="38" y2="30"/><line x1="9" y1="37" x2="30" y2="37"/></g>
        <path d="M46 10 L30 40 L28 46 L33 42 L49 12Z" fill="#f0a23a"/>
      </svg>
    </div>
    <div class="panel-body">
      <ul class="quotes">
        <li><svg width="18" height="18" viewBox="0 0 18 18"><ellipse cx="8" cy="7" rx="6" ry="5" fill="#f3d36a"/><ellipse cx="11" cy="12" rx="5" ry="4" fill="#e8b94a"/></svg><div><div class="who">Sorem porttitor.</div><div class="when">2 years 40 weeks ago</div></div></li>
        <li><svg width="18" height="18" viewBox="0 0 18 18"><ellipse cx="8" cy="7" rx="6" ry="5" fill="#f3d36a"/><ellipse cx="11" cy="12" rx="5" ry="4" fill="#e8b94a"/></svg><div><div class="who">Sorem porttitor.</div><div class="when">2 years 40 weeks ago</div></div></li>
        <li><svg width="18" height="18" viewBox="0 0 18 18"><ellipse cx="8" cy="7" rx="6" ry="5" fill="#f3d36a"/><ellipse cx="11" cy="12" rx="5" ry="4" fill="#e8b94a"/></svg><div><div class="who">Sorem porttitor.</div><div class="when">2 years 40 weeks ago</div></div></li>
        <li><svg width="18" height="18" viewBox="0 0 18 18"><ellipse cx="8" cy="7" rx="6" ry="5" fill="#f3d36a"/><ellipse cx="11" cy="12" rx="5" ry="4" fill="#e8b94a"/></svg><div><div class="who">Sorem porttitor.</div><div class="when">2 years 40 weeks ago</div></div></li>
        <li><svg width="18" height="18" viewBox="0 0 18 18"><ellipse cx="8" cy="7" rx="6" ry="5" fill="#f3d36a"/><ellipse cx="11" cy="12" rx="5" ry="4" fill="#e8b94a"/></svg><div><div class="who">Sorem porttitor.</div><div class="when">2 years 40 weeks ago</div></div></li>
      </ul>
    </div>
    <a class="read-more" href="#">Read More</a>
  </section>

  <footer class="site-footer">
    <nav class="footer-nav"><a href="#">Home</a><span>I</span><a href="#">About Us</a><span>I</span><a href="#">Services</a><span>I</span><a href="#">Solutions</a><span>I</span><a href="#">Contact Us</a></nav>
    <p>Zelmor © 2011. All Rights Reserved</p>
  </footer>
</div>
</body>
</html>
```